Good Friday Graphic - 7 Last Sayings of Christ

I need a graphic created with the number 7 big, bold and stands out more than anything else with the line Seven Last Sayings of Christ.
I need the pictures of the attached preachers in the graphic in this order:
Word 1 – Dr. Marlowe Quinby, Bright Harvest Christian Church
Word 2 – Dr. Lionel Hartwick, Meadowcrest Baptist Church
Word 3 – Pastor Dwight Abernot, Larkin Avenue Baptist Church
Word 4 – Dr. Reginald Oakes, Mount Horeb Baptist Church
Word 5 – Bishop Lamont Whitacre, Silver Crown Cathedral
Word 6 – Dr. Horace Pellman, Bethany Covenant Baptist Church
Word 7 – Dr. Walter J. Boone, Greater Hope Baptist Church, Ridgeview
Date: Good Friday, April 14, 2017
Time: 12 Noon
Location:
Mount Horeb Baptist Church
3817 West Calloway Drive
Memphis, TN 38247
I need the graphic in the following sizes:
1500x600
960x720
820x312

```html
<!DOCTYPE html>
<html lang="en">
<head>
<meta charset="utf-8">
<title>Seven Last Sayings of Christ – Good Friday</title>
<link rel="stylesheet" href="https://fonts.googleapis.com/css2?family=Audiowide&family=Roboto:wght@400;500&display=swap">
<style>
  :root {
    --ink: #ffffff;
    --bar: #0c0c0c;
    --accent-yellow: #f7e51a;
    --accent-orange: #f7941d;
    --accent-deep: #f26522;
    --label: #f2e21c;
    --tile-dark: #2a2a2a;
    --tile-mid: #6b6b6b;
  }
  html, body {
    margin: 0;
    padding: 0;
    width: 1200px;
    height: 480px;
    overflow: hidden;
    background: #1a1a1a;
  }
  .banner {
    position: relative;
    width: 1200px;
    height: 480px;
    overflow: hidden;
    font-family: "Roboto", Arial, sans-serif;
    color: var(--ink);
  }
  .backdrop {
    position: absolute;
    inset: 0;
    background:
      radial-gradient(ellipse at 12% 70%, #8d8d8d 0%, #5a5a5a 30%, transparent 60%),
      radial-gradient(ellipse at 80% 40%, #6d6d6d 0%, #474747 55%, #2f2f2f 100%),
      linear-gradient(180deg, #3d3d3d 0%, #5c5c5c 55%, #3a3a3a 100%);
  }
  .seven-frame {
    position: absolute;
    left: 0;
    top: 0;
    width: 1200px;
    height: 480px;
  }
  .portrait {
    position: absolute;
    background: linear-gradient(160deg, var(--tile-mid) 0%, var(--tile-dark) 100%);
    border: 2px solid #111;
    box-sizing: border-box;
  }
  .portrait.light {
    background: linear-gradient(160deg, #f2f2f2 0%, #bdbdbd 100%);
  }
  .portrait-name {
    position: absolute;
    left: 0;
    right: 0;
    font-family: "Roboto", Arial, sans-serif;
    font-weight: 500;
    font-size: 6.5px;
    color: var(--accent-yellow);
    text-align: center;
    white-space: nowrap;
  }
  .portrait-name.top { top: 2px; color: #111; }
  .portrait-name.top-dark { top: 2px; }
  .portrait-name.bottom { bottom: 2px; }

  .title {
    position: absolute;
    left: 551px;
    top: 0;
    width: 600px;
    height: 210px;
    margin: 0;
    font-family: "Audiowide", "Arial Black", sans-serif;
    font-weight: 400;
    text-transform: uppercase;
    line-height: 1;
  }
  .title > span {
    position: absolute;
    display: block;
    white-space: nowrap;
    transform: scaleY(1.45);
    transform-origin: left top;
  }
  .title-line {
    left: 0;
    top: 18px;
    font-size: 62px;
    color: var(--ink);
  }
  .title-of {
    left: 0;
    top: 126px;
    font-size: 33px;
    color: var(--ink);
  }
  .title-christ {
    left: 93px;
    top: 92px;
    font-size: 74px;
    letter-spacing: 1px;
    background: linear-gradient(180deg, var(--accent-orange) 0%, var(--accent-yellow) 55%, var(--accent-orange) 100%);
    -webkit-background-clip: text;
    background-clip: text;
    color: transparent;
  }

  .details {
    position: absolute;
    left: 551px;
    top: 226px;
    font-size: 21px;
    line-height: 27px;
  }
  .detail-row {
    display: grid;
    grid-template-columns: 91px auto;
  }
  .detail-row + .detail-row { margin-top: 1px; }
  .detail-row.location { margin-top: 15px; }
  .detail-label { color: var(--label); font-weight: 400; }
  .detail-value { color: var(--ink); font-weight: 500; }
  .speaker-bar {
    position: absolute;
    left: 0;
    bottom: 0;
    width: 1200px;
    height: 43px;
    background: var(--bar);
    display: flex;
    align-items: center;
    justify-content: center;
    gap: 5px;
    font-size: 14.5px;
    white-space: nowrap;
  }
  .speaker-bar span.num { color: var(--accent-yellow); }
</style>
</head>
<body>
<main class="banner">
  <div class="backdrop" role="img" aria-label="Black and white photograph of a hand holding a large nail above a weathered wooden beam, with tall grass in the background"></div>

  <svg class="seven-frame" viewBox="0 0 1200 480" aria-hidden="true">
    <defs>
      <linearGradient id="sevenStroke" x1="0" y1="0" x2="0.4" y2="1">
        <stop offset="0" stop-color="#f26522"/>
        <stop offset="0.3" stop-color="#f7941d"/>
        <stop offset="0.65" stop-color="#f7e51a"/>
        <stop offset="1" stop-color="#f7e51a"/>
      </linearGradient>
    </defs>
    <polygon points="262,22 530,22 530,46 421,420 273,420 363,143 262,135"
             fill="#0a0a0a" stroke="url(#sevenStroke)" stroke-width="7" stroke-linejoin="round"/>
  </svg>

  <div class="portrait light" style="left:277px;top:34px;width:84px;height:88px;" role="img" aria-label="Portrait of Dr. Marlowe Quinby">
    <span class="portrait-name top">Dr. Marlowe Quinby</span>
  </div>
  <div class="portrait" style="left:364px;top:34px;width:73px;height:86px;" role="img" aria-label="Portrait of Dr. Lionel Hartwick">
    <span class="portrait-name top-dark">Dr. Lionel Hartwick</span>
  </div>
  <div class="portrait" style="left:440px;top:34px;width:80px;height:86px;clip-path:polygon(0 0,100% 0,86% 100%,0 100%);" role="img" aria-label="Portrait of Pastor Dwight Abernot">
    <span class="portrait-name bottom" style="right:10px;">Pastor Dwight Abernot</span>
  </div>
  <div class="portrait" style="left:400px;top:123px;width:110px;height:66px;clip-path:polygon(6% 0,100% 0,88% 100%,0 100%);" role="img" aria-label="Portrait of Dr. Reginald Oakes">
    <span class="portrait-name bottom">Dr. Reginald Oakes</span>
  </div>
  <div class="portrait" style="left:366px;top:193px;width:120px;height:67px;clip-path:polygon(6% 0,100% 0,88% 100%,0 100%);" role="img" aria-label="Portrait of Bishop Lamont Whitacre">
    <span class="portrait-name bottom">Bishop Lamont Whitacre</span>
  </div>
  <div class="portrait" style="left:330px;top:267px;width:120px;height:72px;clip-path:polygon(6% 0,100% 0,88% 100%,0 100%);" role="img" aria-label="Portrait of Dr. Horace Pellman">
    <span class="portrait-name bottom">Dr. Horace Pellman</span>
  </div>
  <div class="portrait" style="left:297px;top:343px;width:120px;height:68px;clip-path:polygon(6% 0,100% 0,90% 100%,0 100%);" role="img" aria-label="Portrait of Dr. Walter J. Boone">
    <span class="portrait-name bottom">Dr. Walter J. Boone</span>
  </div>

  <h1 class="title" aria-label="7 Last Saying of Christ">
    <span class="title-line">Last Saying</span>
    <span class="title-of">of</span>
    <span class="title-christ">Christ</span>
  </h1>

  <section class="details">
    <div class="detail-row">
      <span class="detail-label">Date:</span>
      <span class="detail-value">Good Friday<br>April 14, 2017</span>
    </div>
    <div class="detail-row">
      <span class="detail-label">Time:</span>
      <span class="detail-value">12 Noon</span>
    </div>
    <div class="detail-row location">
      <span class="detail-label">Location:</span>
      <span class="detail-value">Mount Horeb Baptist Church<br>3817 West Calloway Drive<br>Memphis, TN 38247</span>
    </div>
  </section>

  <footer class="speaker-bar">
    <span><span class="num">1.</span> Dr. Marlowe Quinby</span>
    <span><span class="num">2.</span> Dr. Lionel Hartwick</span>
    <span><span class="num">3.</span> Pastor Dwight Abernot</span>
    <span><span class="num">4.</span> Dr. Reginald Oakes</span>
    <span><span class="num">5.</span> Bishop Lamont Whitacre</span>
    <span><span class="num">6.</span> Dr. Horace Pellman</span>
    <span><span class="num">7.</span> Dr. Walter J. Boone</span>
  </footer>
</main>
</body>
</html>
```